Lenny Marsh Business Cards
DJ Lenny Marsh
Simple
Lenny Marsh
DJ
4731 Corliss Street Los Angeles, CA 90041
djlennymarsh@postvale.com
djlennymarsh.com
I'd like to have a seperate email listing shown as " Bookings - kt@quillsoundagency.com"
-also under website show twitter.com/djlennymarsh
- do not show address on card
Logo on the front all other info on the back
I would like to see the color version titled "lenny-blue-grey" as well as the "lenny-white-grey"
please also try with the color "lenny-black-white". The back of the card should be very simple, nothing too crazy
Please use this logo as well. No need for headphones on the back or any fancy graphics. Please just simple text with the information I provided.Thank you.

```html
<!DOCTYPE html>
<html lang="en">
<head>
<meta charset="utf-8">
<title>Lenny Marsh Business Cards</title>
<link rel="stylesheet" href="https://fonts.googleapis.com/css2?family=Quicksand:wght@500;700&display=swap">
<style>
  :root {
    --page: #ffffff;
    --card: #414449;
    --card-edge: #3a3d42;
    --blue: #1f8fd8;
    --red: #e1322b;
    --ghost: #55585d;
  }
  * { box-sizing: border-box; margin: 0; padding: 0; }
  html, body {
    width: 1200px;
    height: 1057px;
    overflow: hidden;
    background: var(--page);
    font-family: "Quicksand", sans-serif;
  }
  .sheet { position: relative; width: 1200px; height: 1057px; }
  .card {
    position: absolute;
    width: 450px;
    height: 258px;
    background: var(--card);
    border: 1px solid var(--card-edge);
    border-radius: 15px;
    overflow: hidden;
  }
  .card--front-a { left: 168px; top: 213px; }
  .card--back-a  { left: 657px; top: 213px; }
  .card--front-b { left: 168px; top: 591px; }
  .card--back-b  { left: 657px; top: 591px; }

  .wordmark {
    position: absolute;
    left: 0; right: 0; top: 0; bottom: 0;
    display: flex;
    align-items: center;
    justify-content: center;
    gap: 12px;
  }
  .wordmark__dot {
    width: 30px; height: 30px;
    border-radius: 50%;
    background: var(--red);
  }
  .wordmark__name {
    font-weight: 700;
    font-size: 40px;
    letter-spacing: 1px;
    color: var(--blue);
  }

  .back__name {
    position: absolute;
    left: 33px; top: 34px;
    font-weight: 700;
    font-size: 33px;
    color: var(--blue);
    letter-spacing: 0.5px;
  }
  .back__role {
    position: absolute;
    left: 34px; top: 79px;
    font-weight: 700;
    font-size: 20px;
    color: var(--red);
  }
  .back__ghost {
    position: absolute;
    right: 12px; top: 30px;
    width: 190px; height: 190px;
    border-radius: 50%;
    background: var(--ghost);
    opacity: 0.55;
  }
  .contact {
    position: absolute;
    left: 33px;
    list-style: none;
    font-weight: 500;
    font-size: 14px;
    line-height: 21px;
    color: var(--blue);
  }
  .card--back-a .contact { top: 150px; }
  .card--back-b .contact { top: 144px; }
</style>
</head>
<body>
<main class="sheet">

  <section class="card card--front-a" aria-label="Front, lenny-blue-grey">
    <div class="wordmark">
      <span class="wordmark__dot"></span>
      <span class="wordmark__name">LENNY MARSH</span>
    </div>
  </section>

  <section class="card card--back-a" aria-label="Back, version with address">
    <div class="back__ghost" role="img" aria-label="Faint circular backdrop"></div>
    <h2 class="back__name">LENNY MARSH</h2>
    <p class="back__role">DJ</p>
    <ul class="contact">
      <li>4731 Corliss Street Los Angeles, CA 90041</li>
      <li>Cell : 323-555-0187</li>
      <li>Email : djlennymarsh@postvale.com</li>
      <li>Website : www.djlennymarsh.com</li>
    </ul>
  </section>

  <section class="card card--front-b" aria-label="Front, lenny-white-grey">
    <div class="wordmark">
      <span class="wordmark__dot"></span>
      <span class="wordmark__name">LENNY MARSH</span>
    </div>
  </section>

  <section class="card card--back-b" aria-label="Back, bookings version">
    <div class="back__ghost" role="img" aria-label="Faint circular backdrop"></div>
    <h2 class="back__name">LENNY MARSH</h2>
    <p class="back__role">DJ</p>
    <ul class="contact">
      <li>Cell : 323-555-0187</li>
      <li>Email : bookings-kt@quillsoundagency.com</li>
      <li>Website : www.djlennymarsh.com</li>
      <li>Twitter : twitter.com/djlennymarsh</li>
    </ul>
  </section>

</main>
</body>
</html>
```